Voice agent website redesign, responsive. Current website functional, needs fresh look.

** updated 01/04/2015 ** Stock photos and video OK
TQ Sounds is redesigning their website to refresh the look and feel and also to make the website more useable in portable devices.
We also intend to replace our existing iPhone app with responsive HTML.
We want to keep the features but update the way they are displayed.
The current website is at: http://www.tqsounds-demo.com.au. (examples of important pages are in the attachments)
The current website is written in .NET and MS SQL but designs optimised for WordPress will also be accepted.
We have corporate colours and a logo
We want a dynamic element on the front page
We do not mind the idea of a slider, but I must be modern and capable of video backgrounds
We like the clean design of our main competitor: http://www.zelvar-demo.com.au but the site is busy and not responsive.
The site must be designed to use responsive HTML and be easy to see and navigate using smaller viewports.
Once awarded the contract the designer must supply 4 pages in 3 formats, for which we will pay an extra $80, as outlined below:
Submission for selection
Designs must be submitted for selection with 1 required page (home page) in 1 required resolution and 1 optional resolution;
Versions:
• (Required) Full page web landscape – 1920 x 1080
• (Optional) Low resolution portrait (e.g. iPhone 3/4) – 320 x 480
Submission required when awarded
Final supplied designs must have 3 versions of 4 required pages as layered Photoshop files;
Versions:
• Full page web landscape – 1920 x 1080
• Medium resolution landscape (e.g. iPad) – 1024 x 768
• Low resolution portrait (e.g. iPhone 3/4) – 320 x 480
Pages:
• home page
• generic template
• search results
• talent page
The designer may also offer to convert the site into HTML and CSS for an added fee.
The attachments supplied contains important features like site menu and required elements, but only guidelines to design.
Please do read carefully for details on required elements, but do feel free to change the design, look and feel completely.
Attached are;
Target Market(s)
Advertising agencies who hire voice artists, also a showcase for the artists themselves
Look and feel

```html
<!DOCTYPE html>
<html lang="en">
<head>
<meta charset="utf-8">
<title>TQ Sounds – Voice Over Artists</title>
<link rel="stylesheet" href="https://fonts.googleapis.com/css2?family=Roboto:ital,wght@0,400;0,500;0,700;1,400&display=swap">
<style>
:root{
  --navy:#043a63;
  --navy-deep:#022f52;
  --green:#8dc63f;
  --green-dark:#6aa339;
  --white:#ffffff;
  --text:#333333;
  --panel:#eeeeee;
  --link:#2a4e6e;
}
*{box-sizing:border-box;margin:0;padding:0}
html,body{width:904px;height:1200px;overflow:hidden;background:var(--white)}
body{position:relative;font-family:"Roboto",Arial,sans-serif;color:var(--text)}
.abs{position:absolute}

/* header */
.site-header{left:0;top:0;width:904px;height:116px;background:var(--navy)}
.brand{left:106px;top:12px;display:flex;align-items:center;gap:8px;color:var(--white);font-size:26px;font-weight:700;letter-spacing:.5px}
.brand-mark{width:18px;height:18px;background:var(--green)}
.wave-band{left:210px;top:12px;width:590px;height:44px;background:linear-gradient(90deg,rgba(141,198,63,.15),rgba(141,198,63,.85) 35%,rgba(141,198,63,.55) 65%,rgba(141,198,63,.3));opacity:.9}
.tagline{left:548px;top:8px;width:210px;text-align:right;color:var(--white);font-size:19px;letter-spacing:.3px;text-transform:uppercase}
.tagline em{font-style:normal;color:var(--green)}
.header-phones{left:536px;top:61px;width:262px;text-align:right;color:var(--white);font-size:12.5px;word-spacing:1px}
.main-nav{left:106px;top:82px;width:692px;height:34px;background:var(--green);display:flex}
.main-nav a{display:block;padding:0 13px;line-height:34px;color:var(--white);font-size:13.5px;text-decoration:none;text-transform:uppercase}
.main-nav a.is-current{background:var(--white);color:var(--navy);width:73px;text-align:center}

/* hero */
.hero{left:0;top:116px;width:904px;height:359px;background:linear-gradient(100deg,#b9a38a 0%,#6e5c4f 25%,#2d2a2d 45%,#3b3a40 65%,#c9c4bc 100%)}
.slider-arrow{top:294px;width:24px;height:24px;background:rgba(60,60,60,.75)}
.slider-arrow.prev{left:0}.slider-arrow.next{left:880px}
.search-panel{left:575px;top:144px;width:222px;height:300px;background:rgba(4,58,99,.88);border-top:3px solid var(--green);padding:10px 18px}
.field-label{display:block;color:var(--white);font-size:13px;margin-bottom:4px}
.select{height:21px;background:var(--white);font-size:10px;color:#444;padding:0 12px;display:flex;align-items:center;justify-content:space-between;margin-bottom:12px}
.select svg{width:10px;height:7px}
.field-pair{display:flex;justify-content:space-between}
.field-pair .field{width:86px}
.search-button{height:23px;background:#5e9e46;color:var(--white);font-size:13px;text-align:center;line-height:23px;margin-top:2px}

/* about */
.section-title{color:var(--navy);font-weight:500;text-transform:uppercase}
.about{left:106px;top:504px;width:424px}
.about h1{font-size:26px;margin-bottom:16px}
.about p{font-size:13px;line-height:17px;margin-bottom:14px}
.read-more{color:var(--link);font-size:13px;text-decoration:underline}
.testimonials{left:106px;top:808px;width:424px}
.testimonials h2{font-size:22px;margin-bottom:12px}
.quote{position:relative;padding-left:34px;font-style:italic;font-size:12.5px;line-height:18px;width:400px}
.quote svg{position:absolute}
.quote-author{text-align:right;color:var(--navy);font-size:13px;margin-top:14px;width:418px}
.view-all{display:inline-block;margin-top:4px;color:var(--link);font-size:10px;text-decoration:underline}

/* sidebar */
.recent-work{left:546px;top:510px;width:252px;height:214px;background:var(--panel)}
.panel-head{height:34px;background:var(--navy);color:var(--white);text-align:center;line-height:34px;font-size:15px;text-transform:uppercase}
.video{position:relative;margin:9px 7px 0;height:137px;background:linear-gradient(110deg,#3b4a58,#8a9aa6 55%,#d7d4cf)}
.video-play{position:absolute;left:105px;top:55px;width:28px;height:22px;background:rgba(0,0,0,.7);border-radius:4px}
.video-bar{position:absolute;left:0;bottom:0;width:100%;height:12px;background:rgba(0,0,0,.75)}
.caption{font-size:11px;padding:10px 7px;color:#222}
.news{left:546px;top:750px;width:252px;height:194px;background:var(--panel)}
.tabs{display:flex;height:34px;background:var(--white)}
.tab{flex:1;text-align:center;line-height:32px;font-size:14px;text-transform:uppercase}
.tab.is-active{background:var(--navy);color:var(--white)}
.tab.is-idle{border:2px solid var(--navy);color:var(--navy)}
.news-item{display:flex;gap:10px;padding:12px 10px 0}
.news-thumb{width:50px;height:52px;flex:none}
.news-text{font-size:10px;line-height:12px;color:#222}
.news-text a{display:block;margin-top:3px;color:var(--green-dark);font-weight:700;text-decoration:underline}

/* social band */
.follow-bar{left:0;top:978px;width:904px;height:36px;background:var(--green);color:var(--white);font-size:14px}
.follow-bar span{position:absolute;top:7px;display:flex;align-items:center;gap:8px;line-height:22px}
.follow-bar i{display:block;width:22px;height:22px;border-radius:50%;background:var(--white)}

/* footer */
.site-footer{left:0;top:1014px;width:904px;height:186px;background:var(--navy);color:var(--white)}
.footer-brand{left:106px;top:26px;display:flex;align-items:center;gap:8px;font-size:24px;font-weight:700;color:#8aa6bd}
.footer-brand .brand-mark{background:#6aa339}
.copyright{left:106px;top:98px;font-size:11px;line-height:16px;width:160px}
.footer-heading{font-size:15px;padding-bottom:7px;border-bottom:1px solid #9bb1c4}
.contact{left:323px;top:20px;width:215px}
.contact li{list-style:none;position:relative;padding-left:30px;font-size:11.5px;line-height:14px;letter-spacing:.4px;margin-top:14px}
.contact li svg{position:absolute;left:0;top:2px}
.newsletter{left:584px;top:20px;width:214px}
.newsletter p{font-size:11px;line-height:14px;margin-top:12px}
.email-input{margin-top:20px;height:27px;background:var(--white);color:#333;font-size:11px;line-height:27px;padding-left:4px}
.submit{margin:15px 0 0 146px;width:67px;height:26px;border:1px solid var(--white);border-radius:5px;font-size:11px;text-align:center;line-height:24px}
</style>
</head>
<body>

<header class="site-header abs">
  <div class="wave-band abs" role="img" aria-label="Green audio waveform decoration"></div>
  <div class="brand abs"><span class="brand-mark"></span>TQ Sounds</div>
  <div class="tagline abs">Find the <em>right</em> voice.</div>
  <div class="header-phones abs">MEL +61 3 9000 4821 &nbsp; SYD +61 2 9000 6137</div>
</header>
<nav class="main-nav abs">
  <a class="is-current" href="#">Home</a><a href="#">Rates</a><a href="#">About Us</a><a href="#">FAQs</a><a href="#">Payments</a><a href="#">Login</a><a href="#">Contact</a>
</nav>

<section class="hero abs" role="img" aria-label="Photo of a voice artist with headphones speaking into a studio microphone"></section>
<div class="slider-arrow prev abs"><svg width="24" height="24"><path d="M15 6 9 12 15 18" fill="none" stroke="#ddd" stroke-width="1.5"/></svg></div>
<div class="slider-arrow next abs"><svg width="24" height="24"><path d="M9 6 15 12 9 18" fill="none" stroke="#ddd" stroke-width="1.5"/></svg></div>

<form class="search-panel abs">
  <span class="field-label">Serach By Name</span>
  <div class="select">Please Select<svg viewBox="0 0 10 7"><path d="M1 1 5 5 9 1" fill="none" stroke="#333" stroke-width="1.6"/></svg></div>
  <span class="field-label">Location</span>
  <div class="select">Select LOcation<svg viewBox="0 0 10 7"><path d="M1 1 5 5 9 1" fill="none" stroke="#333" stroke-width="1.6"/></svg></div>
  <span class="field-label">Voice Type</span>
  <div class="select">Any<svg viewBox="0 0 10 7"><path d="M1 1 5 5 9 1" fill="none" stroke="#333" stroke-width="1.6"/></svg></div>
  <div class="field-pair">
    <div class="field"><span class="field-label">Language</span><div class="select">Any<svg viewBox="0 0 10 7"><path d="M1 1 5 5 9 1" fill="none" stroke="#333" stroke-width="1.6"/></svg></div></div>
    <div class="field"><span class="field-label">Accent</span><div class="select">Any<svg viewBox="0 0 10 7"><path d="M1 1 5 5 9 1" fill="none" stroke="#333" stroke-width="1.6"/></svg></div></div>
  </div>
  <div class="field-pair">
    <div class="field"><span class="field-label">Sex</span><div class="select">Any<svg viewBox="0 0 10 7"><path d="M1 1 5 5 9 1" fill="none" stroke="#333" stroke-width="1.6"/></svg></div></div>
    <div class="field"><span class="field-label">Age</span><div class="select">Any<svg viewBox="0 0 10 7"><path d="M1 1 5 5 9 1" fill="none" stroke="#333" stroke-width="1.6"/></svg></div></div>
  </div>
  <div class="search-button">Search</div>
</form>

<section class="about abs">
  <h1 class="section-title">About TQ Sounds</h1>
  <p>TQ Sounds is one of Australia’s most successful voice over artists’ agencies. &nbsp;It has long been established as a friendly, professional and high quality Australian agency that has a singular focus on the business of voice overs. The company represents over 120 of Australia’s most exceptional voice artists as well as high profile actors across a wide range of styles, ages, accents, characters and foreign languages.</p>
  <p>The management team of Owen Barkley, Rhea Tomlin and Clara Voss supported by Managing Director Martin Hale and accounts manager Petra Lindqvist all live and breathe voice overs.They are not distracted by repping anyone other than talented, professional voice overs artists.</p>
  <a class="read-more" href="#">Read More</a>
</section>

<section class="testimonials abs">
  <h2 class="section-title">Testimonials</h2>
  <blockquote class="quote">
    <svg style="left:0;top:0" width="24" height="22" viewBox="0 0 24 22"><path d="M0 10Q0 2 9 0V4Q5 5 5 9H10V22H0ZM14 10Q14 2 23 0V4Q19 5 19 9H24V22H14Z" fill="#8dc63f"/></svg>
    Lorem ipsum dolor sit amet, consectetur adipisicing elit, sed do eiusmod tempor incididunt ut labore et dolore magna aliqua. Ut enir ad minim veniam
    <svg style="left:146px;top:38px" width="24" height="22" viewBox="0 0 24 22"><path d="M24 12Q24 20 15 22V18Q19 17 19 13H14V0H24ZM10 12Q10 20 1 22V18Q5 17 5 13H0V0H10Z" fill="#8dc63f"/></svg>
  </blockquote>
  <div class="quote-author">Daniel Ashby</div>
  <a class="view-all" href="#">View All Testimonials</a>
</section>

<aside class="recent-work abs">
  <div class="panel-head">Recent Work</div>
  <div class="video" role="img" aria-label="Video still of a presenter at a radio studio desk">
    <div class="video-play"><svg width="28" height="22"><path d="M11 6 19 11 11 16Z" fill="#fff"/></svg></div>
    <div class="video-bar"></div>
  </div>
  <div class="caption">Nora Eastwood &nbsp;Crumbly Bakes Crispies</div>
</aside>

<aside class="news abs">
  <div class="tabs"><div class="tab is-active">Latest News</div><div class="tab is-idle">TQ Spotlight</div></div>
  <div class="news-item">
    <div class="news-thumb" role="img" aria-label="Children's series title artwork" style="background:#2bb3c8"></div>
    <div class="news-text">The new children’s television series WILLOW featuring Australian legends Josie Marlowe<a href="#">Read More</a></div>
  </div>
  <div class="news-item">
    <div class="news-thumb" role="img" aria-label="Portrait photo of a voice artist" style="background:linear-gradient(#c8c2bb,#2c2c2c)"></div>
    <div class="news-text">The new children’s television series WILLOW featuring Australian legends Josie Marlowe<a href="#">Read More</a></div>
  </div>
</aside>

<div class="follow-bar abs">
  <span style="left:106px">Follow Us At:</span>
  <span style="left:244px"><i></i>Friendwall</span>
  <span style="left:393px"><i></i>Chirpline</span>
  <span style="left:533px"><i></i>Workweb</span>
  <span style="left:690px"><i></i>Circlepage</span>
</div>

<footer class="site-footer abs">
  <div class="footer-brand abs"><span class="brand-mark"></span>TQ Sounds</div>
  <p class="copyright abs">© 2015 Copyright TQ Sounds. All Rights Reserved.</p>
  <div class="contact abs">
    <div class="footer-heading">Contact US</div>
    <ul>
      <li><svg width="16" height="14" viewBox="0 0 16 14"><path d="M8 0 16 7H13V14H10V9H6V14H3V7H0Z" fill="#fff"/></svg>cillum dolore eu fugiat nulla pariatur</li>
      <li style="margin-top:16px"><svg width="14" height="18" viewBox="0 0 14 18"><path d="M3 0 6 4 4 6Q6 11 9 13L11 11 14 14 11 18Q2 14 0 3Z" fill="#fff"/></svg>+61 3 9000 4821<br>+61 2 9000 6137</li>
      <li style="margin-top:18px"><svg width="16" height="11" viewBox="0 0 16 11"><rect width="16" height="11" fill="#fff"/><path d="M0 0 8 6 16 0" fill="none" stroke="#043a63" stroke-width="1.2"/></svg>hello@tqsounds-demo.com</li>
    </ul>
  </div>
  <div class="newsletter abs">
    <div class="footer-heading">Subscribe Newsletter</div>
    <p>Lorem ipsum dolor sit amet, consecterte tur adipisicing elit, sed do</p>
    <div class="email-input">enter email address:</div>
    <div class="submit">Submit</div>
  </div>
</footer>

</body>
</html>
```